Business Card Design Project

We are looking to redesign the logo, business card and stationary of one of our group companies - KESTRAL SUPPLY COMPANY LLC.

The company specialises in industrial PVC and CPVC Piping systems. It is situated in the Middle East and the focus is purely in this region.

The logo work is already completed. The file is uploaded for the reference.

We are looking for a clean minimalistic design for the business card.

regards
Ormund
Updates

Hello Everyone!

Thanks for submitting your designs. 

Yet to find the right design. Probably the below links will give you guys some more idea on what we would like.

Minimalist design with some creativity.

Ormund

http://plaincardgallery.example/inspiration/15-beautifully-minimal-business-cards

http://www.quietlayouthub.example/2011/11/14/30-minimalist-business-card-design/

http://www.firmpixelnotes.example/inspiration/minimal-business-cards/

Target Market(s)

Industrial users

Industry/Entity Type

Industrial

Requirements
Must have
• - Minimalistic design

- Back side of the card should include the manufacturer BRAVOLINE CANADA's decal. The file is upload for the reference

- Further information
Company Name:
KESTRAL SUPPLY COMPANY LLC
Address:
PO Box 9087, Sharjah Industrial Area 5, Qutrani Road
Sharjah, United Arab Emirates
Telephone:
+971-6-5018-392
Fax:
+977-6-5018-393
Email:
mail@ksc-holding.example

- FYI, Kestral Supply Company LLC is the authorised distributor for BRAVOLINE CANADA in the UAE. For further information on bravoline please visit the website www.bravoline.example

```html
<!DOCTYPE html>
<html lang="en">
<head>
<meta charset="utf-8">
<title>Kestral Supply Company LLC – Business Card</title>
<link rel="stylesheet" href="https://fonts.googleapis.com/css2?family=Mulish:wght@400;700&family=Open+Sans:wght@300;400;700&display=swap">
<style>
  :root {
    --page-bg: #f1f2f2;
    --card-dark: #2b2a29;
    --text-light: #e6e6e6;
    --text-soft: #c9c9c9;
    --accent-blue: #8fb4e0;
    --link-blue: #86aee0;
    --row-dark: #8a8a8a;
    --row-light: #d9dada;
    --row-light-text: #7d7d7d;
    --footer-text: #2b2a29;
    --badge-grey: #6a6a6a;
  }
  * { margin: 0; padding: 0; box-sizing: border-box; }
  html, body { width: 1200px; height: 900px; overflow: hidden; }
  body { background: var(--page-bg); position: relative; font-family: "Mulish", sans-serif; }

  .card { position: absolute; width: 525px; height: 300px; box-shadow: 2px 3px 5px rgba(0,0,0,0.25); }

  /* Front */
  .card-front { left: 143px; top: 103px; background: var(--card-dark); color: var(--text-soft); }
  .front-accent { position: absolute; left: 0; top: 182px; width: 12px; height: 100px; background: var(--accent-blue); }
  .brand-mark { position: absolute; left: 28px; top: 182px; width: 104px; height: 100px; display: flex; align-items: center; gap: 6px; }
  .brand-square { width: 16px; height: 16px; background: var(--accent-blue); flex: none; }
  .brand-name { font-family: "Mulish", sans-serif; font-weight: 700; font-size: 14px; letter-spacing: 0.5px; color: var(--text-light); }
  .company-name { position: absolute; right: 19px; top: 64px; font-weight: 700; font-size: 22.5px; letter-spacing: 0.6px; color: var(--text-light); white-space: nowrap; }
  .address { position: absolute; right: 18px; top: 129px; text-align: right; font-size: 16px; line-height: 21.5px; letter-spacing: 1.1px; color: var(--text-soft); }
  .contacts { position: absolute; right: 18px; top: 200px; text-align: right; list-style: none; }
  .contacts li { display: flex; justify-content: flex-end; align-items: center; gap: 4px; color: var(--text-light); }
  .contacts .phone, .contacts .fax { font-size: 18.5px; line-height: 24px; letter-spacing: 0.6px; }
  .contacts .email { font-size: 16px; line-height: 21px; letter-spacing: 0.8px; }
  .contacts .web { font-size: 17px; line-height: 19px; letter-spacing: 1.2px; color: var(--link-blue); }
  .contacts svg { width: 11px; height: 11px; fill: var(--accent-blue); }
  .contacts .web svg { margin-right: 10px; }

  /* Back */
  .card-back { left: 521px; top: 487px; background: #fff; font-family: "Open Sans", sans-serif; font-weight: 300; }
  .back-header { height: 53px; background: var(--card-dark); color: #fff; font-size: 24px; display: flex; align-items: center; justify-content: center; letter-spacing: 0.3px; }
  .services { display: grid; grid-template-columns: 262px 263px; position: relative; }
  .services span { display: flex; align-items: center; justify-content: center; font-size: 23px; }
  .services .dark { background: var(--row-dark); color: #fff; }
  .services .light { background: var(--row-light); color: var(--row-light-text); }
  .services .r1 { height: 38px; } .services .r2 { height: 42px; } .services .r3 { height: 44px; }
  .services .r4 { height: 42px; } .services .r5 { height: 40px; }
  .services .col-right { border-left: 2px solid #9a9a9a; }
  .back-footer { height: 41px; display: flex; align-items: center; justify-content: center; gap: 8px; color: var(--footer-text); }
  .distributor-note { font-size: 11.5px; font-weight: 400; }
  .partner { display: flex; align-items: center; gap: 4px; }
  .partner-dot { width: 20px; height: 20px; border-radius: 50%; background: var(--footer-text); }
  .partner-name { font-weight: 700; font-size: 16px; letter-spacing: -0.3px; }
</style>
</head>
<body>

<section class="card card-front" aria-label="Business card front">
  <div class="front-accent"></div>
  <div class="brand-mark"><span class="brand-square"></span><span class="brand-name">KESTRAL</span></div>
  <h1 class="company-name">KESTRAL SUPPLY COMPANY LLC</h1>
  <p class="address">PO Box 9087, Sharjah Industrial<br>Area 5, Qutrani Road<br>Sharjah, United Arab Emirates</p>
  <ul class="contacts">
    <li class="phone"><svg viewBox="0 0 12 12" aria-hidden="true"><path d="M3 1h2l1 3-1.5 1a6 6 0 0 0 2.5 2.5L8 6l3 1v2c0 1-1 2-2 2A9 9 0 0 1 1 3c0-1 1-2 2-2z"/></svg>+971-6-5018-392</li>
    <li class="fax"><svg viewBox="0 0 12 12" aria-hidden="true"><rect x="3" y="1" width="6" height="3"/><rect x="1" y="4.5" width="10" height="4"/><rect x="3" y="9" width="6" height="2.5"/></svg>+977-6-5018-393</li>
    <li class="email"><svg viewBox="0 0 12 12" aria-hidden="true"><rect x="1" y="2.5" width="10" height="7"/><path d="M1 2.5l5 4 5-4" fill="none" stroke="#2b2a29" stroke-width="1"/></svg>mail@ksc-holding.example</li>
    <li class="web"><svg viewBox="0 0 12 12" aria-hidden="true"><circle cx="6" cy="6" r="5"/><path d="M1 6h10M6 1v10" stroke="#2b2a29" stroke-width="0.8"/></svg>www.bravoline.example</li>
  </ul>
</section>

<section class="card card-back" aria-label="Business card back">
  <h2 class="back-header">COMMUNITY</h2>
  <div class="services">
    <span class="dark r1">PIPES</span><span class="dark r1 col-right">DESIGN</span>
    <span class="light r2">FITTINGS</span><span class="light r2 col-right">LOGISTICS</span>
    <span class="dark r3">VALVES</span><span class="dark r3 col-right">FINANCE</span>
    <span class="light r4">ACCESSORIES</span><span class="light r4 col-right">SOFTWARE</span>
    <span class="dark r5">ENGINEERING</span><span class="dark r5 col-right">INFRASTRUCTURE</span>
  </div>
  <div class="back-footer">
    <span class="distributor-note">Kestral Supply Company LLC, authorised distributor for</span>
    <span class="partner"><span class="partner-dot"></span><span class="partner-name">Bravoline Canada</span></span>
  </div>
</section>

</body>
</html>
```